Web Design for Meadowfield Turf Crew

Meadowfield Turf Crew needs the photoshop files for a simple, clean and professional web design. I need a home and subpage design, although they can be very similar. See pagestridehub.com for a desired layout, although I'd like to see more design than shown on that site. The goal of the site is to attract both lawn maintenance/landscape customers and build a partner network of consultants that serve the US market. The following are needed:

- home and subpage design
- page: Home, Services, Locations, Consultants, FAQ, Contact
- if subpages have header photo, need to include 5 different header photos for each page
- favicon
Updates

I'll award the design based on the homepage concept. The minor subpage changes and other elements can be worked out in the workroom stage. Thanks, Trent

Industry/Entity Type

It Professional

```html
<!DOCTYPE html>
<html lang="en">
<head>
<meta charset="utf-8">
<title>Meadowfield Turf Crew</title>
<link href="https://fonts.googleapis.com/css2?family=Open+Sans:wght@400;600;700&display=swap" rel="stylesheet">
<style>
:root{
  --green:#8cc63f;
  --green-dark:#6fa52a;
  --ink:#3b3b3b;
  --text:#777;
  --light:#f1f1f1;
  --rule:#e2e2e2;
  --nav:#4a4a4a;
  --footer-bar:#333;
  --white:#fff;
}
*{box-sizing:border-box;margin:0;padding:0}
html,body{width:1200px;height:2380px;overflow:hidden}
body{font-family:"Open Sans",Arial,sans-serif;color:var(--text);background:var(--white);position:relative}
.wrap{position:absolute;left:60px;width:1080px}

/* header */
.brand{position:absolute;left:64px;top:34px;display:flex;align-items:center;gap:16px}
.brand-mark{width:54px;height:54px;background:var(--green)}
.brand-name{font-size:34px;font-weight:700;color:var(--ink);line-height:1;letter-spacing:.5px;width:200px}
.top-right{position:absolute;right:62px;top:30px;text-align:right}
.socials{display:flex;gap:8px;justify-content:flex-end}
.socials span{width:26px;height:26px;border-radius:50%;background:#5a8fd0}
.call{position:absolute;right:62px;top:30px;width:150px;text-align:left;padding-left:56px;font-size:14px;color:var(--ink)}
.top-right .socials{margin-right:170px}
.call strong{display:block;color:var(--green);font-size:15px}
.call svg{position:absolute;left:14px;top:2px}

/* nav */
.nav{top:172px;height:44px;background:var(--nav);display:flex;align-items:center;border-radius:3px}
.nav a{color:#ddd;text-decoration:none;font-size:16px;padding:0 36px;height:44px;line-height:44px}
.nav a.active{background:var(--green);color:var(--white)}
.search{margin-left:auto;margin-right:10px;width:190px;height:28px;background:var(--white);border-radius:2px;font-size:13px;color:#999;padding:5px 10px}

/* hero */
.hero{top:232px;height:440px}
.hero-photo{position:absolute;inset:0;background:linear-gradient(180deg,#c9d6c8 0%,#9fb48f 45%,#6f8a55 100%)}
.hero-caption{position:absolute;left:170px;top:112px;background:rgba(40,40,40,.6);color:var(--white);font-size:30px;font-weight:600;padding:4px 16px}
.quote{position:absolute;right:22px;top:64px;width:320px;background:rgba(255,255,255,.85);padding:0 0 16px}
.quote h3{background:var(--green);color:var(--white);font-size:15px;font-weight:700;padding:8px 14px}
.quote .row{display:flex;gap:10px;padding:14px 14px 0}
.field{flex:1;height:30px;background:var(--white);border:1px solid #ccc;font-size:12px;color:#999;padding:6px 8px}
.field.tall{height:110px}
.quote .btns{display:flex;gap:10px;padding:14px 14px 0}
.btn{flex:1;height:32px;line-height:32px;text-align:center;font-size:12px;font-weight:600;color:var(--white);background:#666}

/* welcome */
.welcome{top:712px}
h2{font-size:20px;font-weight:600;color:var(--ink);letter-spacing:1px}
h2 em{font-style:normal;color:var(--green)}
.welcome h2{padding-bottom:22px;border-bottom:1px solid var(--rule)}
.welcome-photo{position:absolute;left:0;top:76px;width:350px;height:230px;background:linear-gradient(160deg,#b7c8a8,#6f8f4c);border:4px solid var(--white);box-shadow:0 0 0 1px var(--rule)}
.welcome-text{position:absolute;left:400px;top:70px;width:680px;font-size:14px;line-height:1.6}
.welcome-text p+p{margin-top:20px}

/* services */
.services-band{position:absolute;left:0;top:1070px;width:1200px;height:690px;border-top:1px solid var(--rule)}
.services{top:1130px;text-align:center}
.services .intro{font-size:14px;line-height:1.6;margin:30px auto 0;width:1040px}
.grid{display:grid;grid-template-columns:repeat(3,1fr);row-gap:60px;margin-top:60px;text-align:left;padding-left:30px}
.item{display:flex;gap:18px}
.icon{flex:none;width:64px;height:64px;border-radius:50%;border:2px solid #ccc;display:flex;align-items:center;justify-content:center}
.item h4{color:var(--green);font-size:17px;font-weight:600;line-height:1.2;margin-bottom:6px}
.item p{font-size:13px;line-height:1.5;width:210px}
.cta{position:absolute;left:480px;top:1672px;width:240px;height:44px;line-height:44px;background:var(--ink);color:var(--white);border-radius:22px;font-size:15px;text-align:center}

/* partners */
.partners{position:absolute;left:0;top:1780px;width:1200px;height:190px;background:var(--light);display:flex;align-items:center;justify-content:space-around;padding:0 80px}
.partners span{background:#bdbdbd;height:56px}

/* footer */
.footer{position:absolute;left:0;top:1990px;width:1200px;height:340px;background:var(--green);color:var(--white)}
.footer h5{font-size:15px;font-weight:700;letter-spacing:1px;padding-bottom:10px;border-bottom:1px solid rgba(255,255,255,.5);margin-bottom:16px}
.col{position:absolute;top:34px}
.map{width:280px;height:186px;background:linear-gradient(135deg,#e7ecd9,#cfd8be)}
.links{display:grid;grid-template-columns:1fr 1fr;font-size:13px;line-height:1.9}
.useful{font-size:13px;line-height:1.9}
.fsocial{display:flex;gap:6px;margin-top:10px}
.fsocial span{width:22px;height:22px;border-radius:50%;background:var(--white)}
.bottom{position:absolute;left:0;top:2330px;width:1200px;height:50px;background:var(--footer-bar);color:#ccc;font-size:13px;text-align:center;line-height:50px}
</style>
</head>
<body>

<header>
  <div class="brand"><span class="brand-mark"></span><span class="brand-name">Meadowfield Turf Crew</span></div>
  <div class="top-right"><div class="socials"><span></span><span></span><span></span><span></span></div></div>
  <div class="call">
    <svg width="30" height="30" viewBox="0 0 24 24"><path d="M6.6 10.8a15 15 0 0 0 6.6 6.6l2.2-2.2a1 1 0 0 1 1-.25 11.4 11.4 0 0 0 3.6.6 1 1 0 0 1 1 1V20a1 1 0 0 1-1 1A17 17 0 0 1 3 4a1 1 0 0 1 1-1h3.5a1 1 0 0 1 1 1c0 1.25.2 2.45.6 3.6a1 1 0 0 1-.25 1z" fill="#3b3b3b"/></svg>
    Call us today<strong>1-800-555-0142</strong>
  </div>
</header>

<nav class="wrap nav">
  <a class="active">Home</a><a>Services</a><a>Locations</a><a>Consultants</a><a>FAQ</a><a>Contact us</a>
  <div class="search">Keyword Search</div>
</nav>

<section class="wrap hero">
  <div class="hero-photo" role="img" aria-label="Crew member pushing a lawn mower across a park lawn with trees behind"></div>
  <div class="hero-caption">Lorem ipsum dolor sample</div>
  <form class="quote">
    <h3>GET A FREE QUOTE</h3>
    <div class="row"><div class="field">Firstname</div><div class="field">Email</div></div>
    <div class="row"><div class="field tall">Message</div></div>
    <div class="btns"><div class="btn">SEND QUOTE</div><div class="btn">RESET FORM</div></div>
  </form>
</section>

<section class="wrap welcome">
  <h2>WELCOME TO <em>MEADOWFIELD TURF CREW</em></h2>
  <div class="welcome-photo" role="img" aria-label="Crew members with ride-on mowers on a green lawn"></div>
  <div class="welcome-text">
    <p>Lorem ipsum dolor sit amet, consectetur adipiscing elit. Vestibulum eget libero ultricies, mattis metus sed, eleifend enim. Ut id feugiat risus. Quisque ac rhoncus mi. Donec euismod dui dui, vitae aliquam justo pharetra vitae. Mauris tempus lorem nisl, in ultrices nulla pretium non.</p>
    <p>Vestibulum ante ipsum primis in faucibus orci luctus et ultrices posuere cubilia Curae; Suspendisse a libero orci. Morbi malesuada libero ut augue pellentesque accumsan. Sed facilisis turpis odio, quis laoreet justo fringilla nec. Sed eleifend euismod mauris vel ornare.</p>
  </div>
</section>

<div class="services-band"></div>
<section class="wrap services">
  <h2>WHAT <em>WE CAN DO</em> FOR YOU</h2>
  <p class="intro">Lorem ipsum dolor sit amet, consectetur adipiscing elit. Vestibulum eget libero ultricies, mattis metus sed, eleifend enim. Ut id feugiat risus. Quisque ac rhoncus mi. Donec euismod dui dui, vitae aliquam justo pharetra vitae. Mauris tempus lorem nisl.</p>
  <div class="grid">
    <div class="item"><div class="icon"><svg width="28" height="28" viewBox="0 0 24 24"><path d="M12 21V9M12 9c0-4 3-6 7-6 0 4-3 6-7 6zM12 13c0-3-2-5-6-5 0 3 2 5 6 5z" fill="none" stroke="#555" stroke-width="2"/></svg></div><div><h4>Landscape Maintenance</h4><p>Lorem ipsum dolor sit amet, consectetur adipiscing elit. Vestibulum eget libero.</p></div></div>
    <div class="item"><div class="icon"><svg width="28" height="28" viewBox="0 0 24 24"><path d="M12 3C9 8 7 11 7 14a5 5 0 0 0 10 0c0-3-2-6-5-11z" fill="none" stroke="#555" stroke-width="2"/></svg></div><div><h4>Irrigation</h4><p>Lorem ipsum dolor sit amet, consectetur adipiscing elit. Vestibulum eget libero.</p></div></div>
    <div class="item"><div class="icon"><svg width="28" height="28" viewBox="0 0 24 24"><path d="M5 12l5 5 9-10" fill="none" stroke="#555" stroke-width="2.4"/></svg></div><div><h4>Fertilization &amp; Plant Health Services</h4><p>Lorem ipsum dolor sit amet, consectetur adipiscing elit. Vestibulum eget libero.</p></div></div>
    <div class="item"><div class="icon"><svg width="28" height="28" viewBox="0 0 24 24"><path d="M12 22s7-7 7-12a7 7 0 0 0-14 0c0 5 7 12 7 12z" fill="none" stroke="#555" stroke-width="2"/><circle cx="12" cy="10" r="2.5" fill="#555"/></svg></div><div><h4>Multi-Location Accounts</h4><p>Lorem ipsum dolor sit amet, consectetur adipiscing elit. Vestibulum eget libero.</p></div></div>
    <div class="item"><div class="icon"><svg width="28" height="28" viewBox="0 0 24 24"><path d="M12 2v20M3 7l18 10M3 17l18-10" stroke="#555" stroke-width="2"/></svg></div><div><h4>Snow &amp; Ice Management</h4><p>Lorem ipsum dolor sit amet, consectetur adipiscing elit. Vestibulum eget libero.</p></div></div>
    <div class="item"><div class="icon"><svg width="28" height="28" viewBox="0 0 24 24"><path d="M4 12h16M14 6l6 6-6 6" fill="none" stroke="#555" stroke-width="2.4"/></svg></div><div><h4>Other Services</h4><p>Lorem ipsum dolor sit amet, consectetur adipiscing elit. Vestibulum eget libero.</p></div></div>
  </div>
</section>
<div class="cta">Contact us today &#8250;</div>

<section class="partners" aria-label="Partners">
  <span style="width:110px;border-radius:50%;height:80px"></span>
  <span style="width:160px"></span>
  <span style="width:150px"></span>
  <span style="width:150px"></span>
  <span style="width:80px;border-radius:50%;height:80px"></span>
</section>

<footer class="footer">
  <div class="col" style="left:70px;width:280px"><h5>LOCATION MAP</h5><div class="map" role="img" aria-label="Street map showing the office location"></div></div>
  <div class="col" style="left:500px;width:280px"><h5>QUICKLINKS</h5>
    <div class="links"><span>Home</span><span>Articles</span><span>About us</span><span>Clients</span><span>What we do</span><span>Partners</span><span>Meet blog</span></div>
  </div>
  <div class="col" style="left:840px;width:290px"><h5>USEFUL INFORMATION</h5>
    <div class="useful">Sitemap<br>F.A.Q.<br>Privacy Policy<br>Terms &amp; Conditions</div>
    <div class="fsocial"><span></span><span></span><span></span><span></span><span></span></div>
  </div>
</footer>
<div class="bottom">Meadowfield Turf Crew. Copyright 2014. All rights reserved.</div>

</body>
</html>
```